STOREFRONT SIGNAGE/ NEW LOGO

Looking for someone to enhance my current sign idea. I own a pawn shop , which is also a gun shop. I want a catchy front sign, which will be a lighted box sign. I may want to incorporate some symbols or character symbology that highlight firearms, such as : guns, ammo, targets, scope retical , gold, diamonds, cash, watches and/or pawn balls, and im open to other ideas, but i do not want it too busy, i want it simple, with a twist. Attached, you will find a very basic design, showing the business name and the verbiage that I would like to be incorporated into the design. God bless and thank you. may the best design win !

```html
<!DOCTYPE html>
<html lang="en">
<head>
<meta charset="utf-8">
<title>Meridian Gold Exchange &amp; Gun Exchange — Storefront Sign</title>
<link rel="stylesheet" href="https://fonts.googleapis.com/css2?family=Archivo:wght@700;800;900&family=Tinos:wght@700&display=swap">
<style>
  :root {
    --backdrop-light: #c2c2c4;
    --backdrop-dark: #a7a7a9;
    --gold-light: #f0c45a;
    --gold-mid: #dca73c;
    --gold-deep: #b9862a;
    --carbon-dark: #0d0d0d;
    --carbon-mid: #262626;
    --ink: #0b0b0b;
    --paper: #ffffff;
    --silver-light: #f2f2f2;
    --silver-dark: #8d8d8d;
    --name-gold: #c99a1c;
  }
  * { box-sizing: border-box; margin: 0; padding: 0; }
  html, body { width: 1200px; height: 826px; overflow: hidden; }
  body {
    background: linear-gradient(120deg, var(--backdrop-dark), var(--backdrop-light));
    font-family: "Archivo", Arial, sans-serif;
    position: relative;
  }
  .sign {
    position: absolute;
    left: 54px; top: 282px;
    width: 1127px; height: 186px;
    box-shadow: 0 14px 22px rgba(0,0,0,.35);
    overflow: hidden;
  }
  .sign-art { position: absolute; inset: 0; }
  .headline {
    position: absolute;
    font-weight: 800;
    font-size: 53px;
    line-height: 50px;
    letter-spacing: -0.5px;
    text-align: center;
  }
  .headline--gold { left: 100px; width: 284px; top: 20px; color: var(--ink); }
  .headline--gun {
    left: 740px; width: 292px; top: 20px;
    background: linear-gradient(180deg, var(--silver-light) 0%, #cfcfcf 45%, var(--silver-dark) 100%);
    -webkit-background-clip: text; background-clip: text; color: transparent;
  }
  .brand-name {
    position: absolute;
    left: 444px; top: 22px; width: 252px; height: 44px;
    display: flex; align-items: center; justify-content: center;
    font-weight: 800; font-size: 34px; letter-spacing: 2px;
    color: var(--name-gold);
  }
  .ampersand {
    position: absolute;
    left: 526px; top: 82px; width: 56px; height: 56px;
    border-radius: 50%;
    background: var(--paper);
    border: 3px solid var(--gold-mid);
    display: flex; align-items: center; justify-content: center;
    font-weight: 900; font-size: 30px; color: var(--ink);
  }
  .service-list {
    position: absolute;
    display: flex; align-items: center;
    font-weight: 800; font-size: 15px; color: var(--ink);
    white-space: nowrap;
    height: 34px;
  }
  .service-list--pawn { left: 42px; top: 138px; gap: 9px; }
  .service-list--goods { left: 659px; top: 138px; gap: 6px; }
  .divider { font-weight: 400; font-size: 13px; }
  .chevron { font-size: 17px; margin-right: -4px; }
  .dot { display: inline-block; width: 6px; height: 6px; border-radius: 50%; background: var(--ink); margin-right: -2px; }
  .size-caption {
    position: absolute;
    left: 0; width: 1148px; top: 530px;
    text-align: center;
    font-family: "Tinos", "Times New Roman", serif;
    font-weight: 700; font-size: 47px; color: var(--ink);
  }
</style>
</head>
<body>
  <section class="sign" aria-label="Meridian Gold Exchange and Gun Exchange storefront sign">
    <svg class="sign-art" width="1127" height="186" viewBox="0 0 1127 186" aria-hidden="false">
      <defs>
        <linearGradient id="gold-foil" x1="0" y1="0" x2="1" y2="1">
          <stop offset="0" stop-color="var(--gold-mid)"/>
          <stop offset="0.45" stop-color="var(--gold-light)"/>
          <stop offset="1" stop-color="var(--gold-deep)"/>
        </linearGradient>
        <linearGradient id="carbon" x1="0" y1="0" x2="1" y2="1">
          <stop offset="0" stop-color="var(--carbon-mid)"/>
          <stop offset="1" stop-color="var(--carbon-dark)"/>
        </linearGradient>
      </defs>
      <rect class="gold-panel" role="img" aria-label="Textured gold foil background" x="0" y="0" width="1127" height="186" fill="url(#gold-foil)"/>
      <polygon class="carbon-panel" role="img" aria-label="Carbon fibre weave background" points="602,0 1127,0 1127,186 526,186" fill="url(#carbon)"/>
      <polygon class="service-band" points="0,139 468,139 484,172 0,172" fill="var(--paper)"/>
      <polygon class="service-band" points="641,139 1127,139 1127,173 661,173" fill="var(--paper)"/>
    </svg>

    <h1 class="headline headline--gold">Gold<br>Exchange</h1>
    <div class="brand-name">MERIDIAN</div>
    <div class="ampersand">&amp;</div>
    <h2 class="headline headline--gun">Gun<br>Exchange</h2>

    <div class="service-list service-list--pawn">
      <span>PAWN</span><span class="divider">|</span>
      <span class="chevron">»</span><span>BUY</span><span class="divider">|</span>
      <span class="chevron">»</span><span>SELL</span><span class="divider">|</span>
      <span class="chevron">»</span><span>TRADE</span><span class="divider">|</span>
      <span class="chevron">»</span><span>LAYAWAY</span>
    </div>

    <div class="service-list service-list--goods">
      <span>GUNS</span><span class="divider">|</span>
      <span class="dot"></span><span>GOLD</span><span class="divider">|</span>
      <span class="dot"></span><span>JEWELRY</span><span class="divider">|</span>
      <span class="dot"></span><span>DIAMONDS</span><span class="divider">|</span>
      <span class="dot"></span><span>WATCHES</span>
    </div>
  </section>

  <p class="size-caption">Height 5 feet and Width 30 feet</p>
</body>
</html>
```